Brochure for a conference with healthcare professionals

Creating a brochure with the information provided in the word document attached below.. along with the logo.. All the information for the brochure is in the word document.. I attached a logo of endocrinology dept in the files.. Use that logo more promintenly than the brenmore care logo..

Most of the designs submitted till now didn't understand what was written on the word document.. The tri-fold should be designed to tell a story.. it should capture the attention just by its title.. then all the information provided should hook them in..

Target Market(s)

Physicians and CEOs of hospitals

Industry/Entity Type

Healthcare

Font styles to use
Serif

Colors

Designer to choose colors to be used in the design.

Requirements
Must have
• Good and memorable design with pictures and elegant design.. The design I am expecting is a tri-fold 9x16 size that can be tested on quellorint.example..

```html
<!DOCTYPE html>
<html lang="en">
<head>
<meta charset="utf-8">
<title>Brenmore Care – Tele-Endocrinology Tri-fold</title>
<link href="https://fonts.googleapis.com/css2?family=Oswald:wght@500;700&family=Open+Sans:wght@400;600;700&display=swap" rel="stylesheet">
<style>
  :root{
    --orange:#f7a21b;
    --orange-deep:#ee8c12;
    --grey:#8a8a8a;
    --grey-dark:#5e5e5e;
    --grey-light:#e9e9e9;
    --ink:#2b2b2b;
    --white:#ffffff;
    --bg:#d9d9d9;
  }
  *{box-sizing:border-box;margin:0;padding:0}
  html,body{width:1200px;height:1200px;overflow:hidden;background:var(--bg);font-family:"Open Sans",Arial,sans-serif;color:var(--ink)}
  .sheet{position:absolute;left:60px;width:1080px;height:540px;display:flex;box-shadow:0 6px 18px rgba(0,0,0,.18)}
  .sheet--outside{top:40px}
  .sheet--inside{top:620px}
  .panel{position:relative;width:360px;height:540px;overflow:hidden;background:linear-gradient(180deg,#fff 0%,#f1f1f1 100%)}
  .panel + .panel{border-left:1px solid rgba(0,0,0,.06)}
  .shapes{position:absolute;inset:0;width:100%;height:100%}
  .photo{position:absolute}
  .heading{font-family:"Oswald",Arial,sans-serif;font-weight:700;text-transform:uppercase;letter-spacing:.3px;line-height:1.05}
  .heading--underlined{border-bottom:2px solid var(--ink);display:inline-block;padding-bottom:2px}
  .ticks{list-style:none}
  .ticks li{position:relative;padding-left:16px;font-size:10.5px;line-height:1.35;margin-bottom:2px}
  .ticks li::before{content:"";position:absolute;left:0;top:3px;width:9px;height:9px;border:1px solid currentColor}
  .ticks li::after{content:"";position:absolute;left:3px;top:3px;width:3px;height:6px;border:solid currentColor;border-width:0 1.5px 1.5px 0;transform:rotate(45deg)}

  /* outside – left */
  .helps{position:absolute;left:28px;top:100px;width:310px;z-index:1}
  .helps .heading{font-size:16px;margin-bottom:8px}
  .also{margin-top:12px}
  .photo--organ{left:0;bottom:0;width:360px;height:70px;background:radial-gradient(ellipse at 65% 60%,#d9544a 0%,#c8d9e8 35%,#eef2f5 75%)}

  /* outside – middle */
  .price-tag{position:absolute;left:60px;top:0;width:140px;padding:16px 0 12px;background:var(--grey);color:#fff;text-align:center;font-size:20px;box-shadow:0 4px 8px rgba(0,0,0,.2)}
  .contact-title{position:absolute;left:40px;top:110px;color:#fff;font-size:30px}
  .contact-sub{position:absolute;left:70px;top:155px;color:#fff;font-size:14px;font-weight:600}
  .photo--desk{left:0;top:250px;width:360px;height:290px;background:linear-gradient(135deg,#eef3f6 0%,#f6efe9 50%,#eaf0f3 100%);opacity:.9}
  .contact{position:absolute;left:0;top:280px;width:360px;text-align:center;font-size:15px}
  .contact p{margin-bottom:4px}
  .contact svg{display:block;margin:8px auto 4px}
  .contact .clinic{font-size:17px;font-weight:600;line-height:1.3;margin-top:6px}

  /* outside – right */
  .brand{position:absolute;left:40px;top:24px;display:flex;align-items:center;gap:8px;font-size:18px;font-weight:600;color:var(--orange-deep)}
  .brand i{display:block;width:18px;height:18px;border-radius:50%;background:var(--orange)}
  .photo--exam{left:40px;top:70px;width:300px;height:190px;background:linear-gradient(120deg,#f1dcd2 0%,#e04f9d 45%,#f5f5f5 70%,#2a2a2a 100%)}
  .cover-title{position:absolute;left:30px;top:330px;width:300px;color:#fff;text-align:center}
  .cover-title .heading{font-size:32px}
  .cover-title p{margin-top:16px;font-size:14px;line-height:1.35}
  .frame{position:absolute;border:2px dashed rgba(255,255,255,.7)}

  /* inside – left */
  .photo--doctor{left:0;top:0;width:360px;height:380px;background:linear-gradient(160deg,#f4f4f4 0%,#dfe4e8 50%,#c9ced2 100%)}
  .fee-band{position:absolute;left:0;top:366px;width:360px;padding:8px 18px;background:var(--orange);color:#fff;font-size:15px}
  .process{position:absolute;left:18px;top:420px;width:330px}

  /* inside – middle */
  .partner-title{position:absolute;left:24px;top:36px;width:320px;font-size:16px;color:var(--ink)}
  .partner-strip{position:absolute;left:20px;top:84px;width:300px;padding:4px 12px;background:var(--grey);color:#fff;font-size:12px;font-weight:600}
  .advantages{position:absolute;left:24px;top:116px;width:320px}
  .how{position:absolute;left:24px;top:262px;width:320px}
  .how .heading{font-size:15px;margin-bottom:6px}
  .photo--pills{left:130px;top:465px;width:110px;height:50px;border-radius:50%;background:radial-gradient(circle,#e8c24a 0%,#cf4a3a 40%,#d6d6d6 75%)}

  /* inside – right */
  .commute{position:absolute;left:40px;top:40px;width:290px;text-align:center}
  .commute .heading{font-size:22px;margin-bottom:10px}
  .commute p{font-size:12.5px;line-height:1.35}
  .circles{position:absolute;left:60px;top:150px;display:flex;gap:14px}
  .circles span{width:66px;height:66px;border-radius:50%;border:3px solid var(--orange);background:radial-gradient(circle,#f2d9c4 0%,#c98b5c 100%)}
  .byline{position:absolute;left:30px;top:240px;width:300px;text-align:center;font-size:14px;font-weight:600;line-height:1.35}
  .photo--ward{left:0;top:330px;width:360px;height:210px;background:linear-gradient(135deg,#c9d4e4 0%,#8ea0bf 50%,#6d5f58 100%)}
</style>
</head>
<body>

<section class="sheet sheet--outside">
  <div class="panel panel--services">
    <svg class="shapes" viewBox="0 0 360 540" aria-hidden="true">
      <polygon points="0,0 360,0 360,20 0,85" fill="#f7a21b"/>
      <polygon points="220,0 360,0 360,55 280,70" fill="#8a8a8a"/>
    </svg>
    <div class="photo photo--organ" role="img" aria-label="Gloved hand holding a scalpel beside an anatomical organ model"></div>
    <div class="helps">
      <h2 class="heading heading--underlined">Tele-Endocrinology helps in</h2>
      <ul class="ticks">
        <li>Management of type 1 and type 2 diabetes.</li>
        <li>Hypothyroidism, hyperthyroidism, thyroid cancer, thyroid nodules</li>
        <li>Bone disease (Osteoporosis and pagets disease</li>
        <li>Adrenal disorders</li>
        <li>Pituitary tumors</li>
        <li>Polycystic ovarian disease</li>
        <li>Obesity and weight loss</li>
        <li>Calcium disorders (hyperparathyroidism and hypoparathyroidism)</li>
        <li>Male hypogonadism (testosterone replacements)</li>
        <li>Transgender hormone treatment</li>
        <li>Multiple endocrine neoplasia</li>
      </ul>
      <div class="also">
        <h2 class="heading heading--underlined">Also available</h2>
        <ul class="ticks">
          <li>ADA certified Diabetes Education by Certified Diabetic Educator</li>
          <li>Nutritionist service</li>
        </ul>
      </div>
    </div>
  </div>

  <div class="panel panel--contact">
    <svg class="shapes" viewBox="0 0 360 540" aria-hidden="true">
      <polygon points="0,0 360,0 360,210 0,250" fill="#f7a21b"/>
      <polygon points="0,250 360,210 360,235 110,300" fill="#8a8a8a"/>
      <line x1="330" y1="110" x2="330" y2="200" stroke="#fff" stroke-width="2" stroke-dasharray="6 6"/>
      <line x1="20" y1="20" x2="20" y2="80" stroke="#5e5e5e" stroke-width="2" stroke-dasharray="6 6"/>
    </svg>
    <div class="photo photo--desk" role="img" aria-label="Soft-focus desk with medical supplies"></div>
    <div class="price-tag heading">$25 per<br>patient</div>
    <h2 class="contact-title heading">Contact us</h2>
    <p class="contact-sub">Brenmore Care</p>
    <div class="contact">
      <svg width="14" height="14" viewBox="0 0 24 24" aria-hidden="true"><path fill="#2b2b2b" d="M6.6 10.8a15 15 0 0 0 6.6 6.6l2.2-2.2c.3-.3.7-.4 1-.2 1.1.4 2.3.6 3.6.6.6 0 1 .4 1 1V20c0 .6-.4 1-1 1A17 17 0 0 1 3 4c0-.6.4-1 1-1h3.5c.6 0 1 .4 1 1 0 1.3.2 2.5.6 3.6.1.3 0 .7-.2 1z"/></svg>
      <p>555-014-2210</p>
      <p>1-800-555-0142</p>
      <svg width="16" height="12" viewBox="0 0 24 18" aria-hidden="true"><rect width="24" height="18" rx="2" fill="#2b2b2b"/><path d="M1 2l11 8 11-8" stroke="#fff" stroke-width="2" fill="none"/></svg>
      <p>dana@brenmore-care.example</p>
      <svg width="12" height="16" viewBox="0 0 12 16" aria-hidden="true"><path fill="#2b2b2b" d="M6 0a6 6 0 0 0-6 6c0 4.5 6 10 6 10s6-5.5 6-10a6 6 0 0 0-6-6zm0 8.5A2.5 2.5 0 1 1 6 3.5a2.5 2.5 0 0 1 0 5z"/></svg>
      <p class="clinic">Westfield Endocrinology and<br>Metabolic Medicine, Riverton</p>
    </div>
  </div>

  <div class="panel panel--cover">
    <svg class="shapes" viewBox="0 0 360 540" aria-hidden="true">
      <polygon points="0,240 200,300 360,200 360,540 0,540" fill="#f7a21b"/>
      <polygon points="0,210 200,290 360,170 360,200 200,300 0,240" fill="#8a8a8a"/>
    </svg>
    <div class="brand"><i></i>Brenmore Care</div>
    <div class="photo photo--exam" role="img" aria-label="Doctor examining a patient's thyroid"></div>
    <div class="frame" style="left:16px;top:300px;width:328px;height:200px"></div>
    <div class="cover-title">
      <h1 class="heading">Tele-Endocrinology<br>Service</h1>
      <p>by Westfield Endocrinology<br>and Metabolic Medicine</p>
    </div>
  </div>
</section>

<section class="sheet sheet--inside">
  <div class="panel panel--process">
    <div class="photo photo--doctor" role="img" aria-label="Doctor holding a green apple and a bathroom scale"></div>
    <div class="fee-band heading">Covered by Originating Site Fee<br>(about $25 per patient).</div>
    <ul class="ticks process">
      <li>Appointment made via Web Portal or by calling our clinic</li>
      <li>Apps offered within 24 hours both for In-patient and Out-patients</li>
      <li>Patient meets endocrinologist at partner Clinic via telemedicine portal.</li>
      <li>Patient is accompanied by a MA during the appointment</li>
      <li>Patient Notes are faxed electronically to the partner clinic.</li>
    </ul>
  </div>

  <div class="panel panel--partners" style="background:linear-gradient(180deg,#f7a21b 0%,#f39a17 100%)">
    <svg class="shapes" viewBox="0 0 360 540" aria-hidden="true">
      <polygon points="0,445 360,405 360,540 0,540" fill="#e3e3e3"/>
      <polygon points="0,425 360,385 360,410 0,455" fill="#8a8a8a"/>
    </svg>
    <h2 class="partner-title heading heading--underlined">FQHC, RHC, CAH, Primary Care physicians can partner with us</h2>
    <div class="partner-strip">Advantages to our Partners</div>
    <ul class="ticks advantages">
      <li>Provide Endocrinologist in their own clinic</li>
      <li>Provide Diabetes Education and Nutritionist Services in their clinic</li>
      <li>Improve convenience to patients and reduce wait-time</li>
      <li>No setup cost and low on-going Expenses</li>
      <li>Can be CashFlow Positive</li>
      <li>Use the technology to widen the reach of their own employed physicians.</li>
    </ul>
    <div class="how">
      <h2 class="heading heading--underlined">How does it work?</h2>
      <ul class="ticks">
        <li>No Special equipment needed.</li>
        <li>Existing Computers with integrated VideoCam used.</li>
        <li>Endocrinologist bills Insurance directly</li>
        <li>HIPAA Compliant Telehealth Portal ($300 / Month).</li>
      </ul>
    </div>
    <div class="photo photo--pills" role="img" aria-label="Spoon of colourful capsules"></div>
  </div>

  <div class="panel panel--commute">
    <svg class="shapes" viewBox="0 0 360 540" aria-hidden="true">
      <polyline points="200,12 340,12 340,60" stroke="#5e5e5e" stroke-width="2" fill="none"/>
      <line x1="340" y1="200" x2="340" y2="260" stroke="#5e5e5e" stroke-width="2" stroke-dasharray="6 6"/>
    </svg>
    <div class="commute">
      <h2 class="heading heading--underlined">Save on commute</h2>
      <p>Control Diabetes and Thyroid Disorders Decrease Wait-times for an Endocrinologist Achieve Weight loss</p>
    </div>
    <div class="circles">
      <span role="img" aria-label="Glucose finger-prick test"></span>
      <span role="img" aria-label="Thyroid check at the neck"></span>
      <span role="img" aria-label="Measuring tape around a waist"></span>
    </div>
    <p class="byline">by Westfield Endocrinology<br>and Metabolic Medicine</p>
    <div class="photo photo--ward" role="img" aria-label="Doctor visiting a patient in a hospital bed"></div>
    <svg class="shapes" viewBox="0 0 360 540" aria-hidden="true">
      <polygon points="0,330 360,300 360,330 140,400 0,380" fill="#5e5e5e"/>
      <polygon points="0,380 140,400 0,470" fill="#8a8a8a"/>
    </svg>
  </div>
</section>

</body>
</html>
```